Alcohol free flavoured Malt Drink Label design

we are beverage company producer our main brand is Brightwave, we are willing to produce Alcohol free flavoured Malt Drink, this product target new generation should be fresh colourful and modern, the name of the Malt drink is Zeal. so main brand is Brightwave and product name is ZEAL. the label size: 198mm X 66mm

Dear All
i changed the product name to NUR (means Crown ) this will add more ideas in the design . Thanks

```html
<!DOCTYPE html>
<html lang="en">
<head>
<meta charset="utf-8">
<title>NUR Malt Drink – Label Set</title>
<link rel="stylesheet" href="https://fonts.googleapis.com/css2?family=Alfa+Slab+One&family=Montserrat:wght@700;800&display=swap">
<style>
  :root {
    --backdrop: #dcf79a;
    --sunset-magenta: #d41a7c;
    --sunset-red: #c8283e;
    --sunset-orange: #e8a24a;
    --sunset-yellow: #f1e43a;
    --sunset-lime: #9fd04a;
    --sky-light: #a8d4f0;
    --sky-mid: #78b8e6;
    --sky-deep: #2f8cc8;
    --ember-orange: #d8782e;
    --ember-dark: #c06a2a;
    --gold: #f8d838;
    --badge-yellow: #f6e04a;
    --badge-pale: #cfe6f8;
    --berry: #c2187a;
    --white: #ffffff;
    --mint-text: #6fbf4a;
  }
  * { box-sizing: border-box; margin: 0; padding: 0; }
  html, body { width: 900px; height: 1200px; overflow: hidden; }
  body {
    background: var(--backdrop);
    font-family: "Montserrat", sans-serif;
    display: flex;
    flex-direction: column;
    align-items: center;
    justify-content: center;
    gap: 60px;
  }
  .label {
    position: relative;
    width: 780px;
    height: 260px;
    overflow: hidden;
  }
  .label__art { position: absolute; inset: 0; }
  .label--sunset .label__art {
    background:
      radial-gradient(circle at 100% 100%, var(--sunset-lime) 0%, transparent 45%),
      linear-gradient(180deg, var(--sunset-magenta) 0%, var(--sunset-red) 35%, var(--sunset-orange) 65%, var(--sunset-yellow) 100%);
  }
  .label--sky .label__art {
    background: radial-gradient(circle at 50% 50%, var(--sky-light) 30%, var(--sky-mid) 120%);
  }
  .label--ember .label__art {
    background: radial-gradient(circle at 50% 50%, var(--ember-orange) 35%, var(--ember-dark) 120%);
  }
  .label__content {
    position: absolute;
    inset: 0;
    display: flex;
    flex-direction: column;
    align-items: center;
  }
  .brand-tab {
    position: absolute;
    left: 208px;
    top: 0;
    padding: 10px 18px 12px;
    border-radius: 0 0 16px 16px;
    font-weight: 800;
    font-size: 20px;
    letter-spacing: 0.01em;
  }
  .label--sunset .brand-tab,
  .label--ember .brand-tab { background: var(--badge-yellow); color: var(--berry); }
  .label--sky .brand-tab { background: var(--badge-pale); color: var(--sky-deep); }
  .product-name {
    margin-top: 62px;
    font-family: "Alfa Slab One", serif;
    font-size: 112px;
    line-height: 1;
    letter-spacing: 0.02em;
  }
  .label--sunset .product-name,
  .label--ember .product-name { color: var(--gold); }
  .label--sky .product-name { color: var(--sky-deep); }
  .product-type {
    margin-top: 10px;
    font-weight: 800;
    font-size: 17px;
    letter-spacing: 0.62em;
    padding-left: 0.62em;
  }
  .label--sunset .product-type,
  .label--ember .product-type { color: var(--gold); }
  .label--sky .product-type { color: var(--white); }
  .volume {
    margin-top: 12px;
    font-weight: 700;
    font-size: 11px;
    letter-spacing: 0.06em;
    color: var(--mint-text);
  }
</style>
</head>
<body>
  <section class="label label--sunset">
    <div class="label__art" role="img" aria-label="Bubble pattern over a magenta to yellow and lime gradient"></div>
    <div class="label__content">
      <span class="brand-tab">Brightwave</span>
      <h1 class="product-name">NUR</h1>
      <p class="product-type">MALT DRINK</p>
      <p class="volume">335 ML</p>
    </div>
  </section>

  <section class="label label--sky">
    <div class="label__art" role="img" aria-label="Bubble pattern in light and mid blue"></div>
    <div class="label__content">
      <span class="brand-tab">Brightwave</span>
      <h2 class="product-name">NUR</h2>
      <p class="product-type">MALT DRINK</p>
    </div>
  </section>

  <section class="label label--ember">
    <div class="label__art" role="img" aria-label="Bubble pattern in warm orange tones"></div>
    <div class="label__content">
      <span class="brand-tab">Brightwave</span>
      <h2 class="product-name">NUR</h2>
      <p class="product-type">MALT DRINK</p>
    </div>
  </section>
</body>
</html>
```